Brixel Information Technology Solutions
We are an Information Technology Company. We provide computer services to commercial companies. We would like a new card full color front and back with bleeding edge.
We have a logo that you can use or if you want to come up with a new logo that is fine too.
Our colors are mostly Maroon and black but be creative.
Sample Information
Grant P Oswick
4818 W Saguaro Ridge Drive
Suite 410
Saguaro Falls, AZ 85099
O: 602.555.0143
C: 602.555.0178
24/7: 888.555.0162
goswick@brixelit.com
www.brixelit.com
Target Market(s)
Business of all sizes
Industry/Entity Type
Computer
Requirements
Must have
- Bleeding edge
full color on both sides

```html
<!DOCTYPE html>
<html lang="en">
<head>
<meta charset="utf-8">
<title>Brixel Business Card</title>
<link rel="stylesheet" href="https://fonts.googleapis.com/css2?family=PT+Sans:wght@400&display=swap">
<style>
  :root {
    --ink-black: #070808;
    --brand-red: #c8060f;
    --brand-red-glow: #f0172e;
    --brand-red-deep: #b8040d;
    --slate: #5b6469;
    --paper: #ffffff;
  }
  * { margin: 0; padding: 0; box-sizing: border-box; }
  html, body { width: 1125px; height: 1200px; overflow: hidden; background: var(--ink-black); }
  body { font-family: "PT Sans", Tahoma, sans-serif; }

  .card-front {
    position: absolute; left: 0; top: 0; width: 1125px; height: 598px;
    background: var(--ink-black);
  }
  .front-panel {
    position: absolute; left: 37px; top: 37px; width: 1049px; height: 525px;
    background: radial-gradient(ellipse at 50% 50%, var(--brand-red-glow) 0%, var(--brand-red) 60%, var(--brand-red-deep) 100%);
  }
  .logo-band {
    position: absolute; left: 37px; top: 185px; width: 1049px; height: 230px;
    background: var(--paper);
    box-shadow: 0 2px 6px rgba(0,0,0,0.25), 0 -2px 6px rgba(0,0,0,0.25);
    text-align: center; color: var(--slate);
  }
  .brand-name {
    display: block; margin-top: 22px;
    font-size: 112px; letter-spacing: 48px; line-height: 1; padding-left: 48px;
  }
  .brand-tagline {
    display: block; margin-top: 12px;
    font-size: 44px; letter-spacing: 2.5px; line-height: 1;
  }

  .card-back {
    position: absolute; left: 0; top: 600px; width: 1125px; height: 600px;
    background: radial-gradient(ellipse at 50% 50%, var(--brand-red-glow) 0%, var(--brand-red) 60%, var(--brand-red-deep) 100%);
    border-top: 1px solid #e8e8e8;
  }
  .side-tabs { position: absolute; left: 0; top: 0; width: 1125px; height: 600px; }
  .tab-shape { fill: var(--paper); }
  .tab-label { fill: var(--slate); font-family: "PT Sans", Tahoma, sans-serif; font-size: 38px; letter-spacing: 14px; }

  .contact-name {
    position: absolute; left: 240px; top: 40px;
    color: var(--paper); font-size: 100px; font-weight: 400; line-height: 1;
  }
  .contact-details {
    position: absolute; left: 242px; top: 175px;
    color: var(--paper); font-size: 36px; line-height: 46px; list-style: none;
  }
</style>
</head>
<body>
  <section class="card-front">
    <div class="front-panel"></div>
    <div class="logo-band">
      <span class="brand-name">BRIXEL</span>
      <span class="brand-tagline">Information Technology Solutions</span>
    </div>
  </section>

  <section class="card-back">
    <svg class="side-tabs" viewBox="0 0 1125 600" width="1125" height="600">
      <path class="tab-shape" d="M0,125 L132,282 Q148,300 132,318 L0,475 Z"/>
      <path class="tab-shape" d="M1125,125 L993,282 Q977,300 993,318 L1125,475 Z"/>
      <text class="tab-label" transform="translate(42,300) rotate(-90)" text-anchor="middle">BRIXEL</text>
      <text class="tab-label" transform="translate(1084,300) rotate(90)" text-anchor="middle">BRIXEL</text>
    </svg>
    <h1 class="contact-name">Grant P Oswick</h1>
    <ul class="contact-details">
      <li>4818 W Saguaro Ridge Drive</li>
      <li>Suite 410</li>
      <li>Saguaro Falls, AZ 85099</li>
      <li>O: 602.555.0143</li>
      <li>C: 602.555.0178</li>
      <li>24/7: 888.555.0162</li>
      <li>goswick@brixelit.com</li>
      <li>www.brixelit.com</li>
    </ul>
  </section>
</body>
</html>
```